Postcard Front / Back For Computer Store with IT services

We are a computer store located in Hawaii on the island of Kauai. We would like to have a post card designed to market our services that we offer. We are a PC and Mac repair shop with full retail services.website: www.pkbytes.com the first thing that comes up is our service plan, we would like to market that, if you notice we have it Hawaii, meaning the background matches where we live etc, we would like to have the post card themed Hawaii.We offer a bunch of different Service contract Options for our customers:Signle computer 24.99/month Family Plan 29.99/month Business Plan 49.99/per computer month We also offer backup services much like vaultmoss but our own brand starting at 9.99/month.

website address https://www.pkbytes.com/online-backup/ for backup offerings..

Target Market(s)

Computer repair, IT services, Online backup, Remote Help Desk

Industry/Entity Type

Computer Repair

Requirements
Must have
• Should have front and Back color
• Phone number 808-317-4962
• website address www.pkbytes.com
Nice to have
• Google map with location on map
• Store hours mon - friday 9am - 6pm

```html
<!DOCTYPE html>
<html lang="en">
<head>
<meta charset="utf-8">
<title>PK Bytes Kauai – Postcard Front and Back</title>
<link rel="stylesheet" href="https://fonts.googleapis.com/css2?family=Fjalla+One&family=Open+Sans:wght@400;600;700&display=swap">
<style>
:root{
  --green:#3fa843;
  --green-dark:#2e8f35;
  --blue:#2aa3c6;
  --blue-dark:#1b86a8;
  --ink:#1f2a30;
  --dark-band:#262626;
  --paper:#ffffff;
  --grey-wash:#eceeef;
  --bg:#d9d4cc;
}
*{box-sizing:border-box;margin:0;padding:0}
html,body{width:1200px;height:1121px;overflow:hidden;background:var(--bg)}
body{position:relative;font-family:"Open Sans",Arial,sans-serif;color:var(--ink)}
.card{position:absolute;background:linear-gradient(180deg,var(--paper) 0%,var(--paper) 35%,var(--grey-wash) 100%);box-shadow:0 6px 18px rgba(0,0,0,.25);overflow:hidden}
.card-front{left:30px;top:20px;width:720px;height:530px}
.card-back{left:450px;top:564px;width:720px;height:550px}
.heading{font-family:"Fjalla One","Arial Narrow",sans-serif;font-weight:400}
.abs{position:absolute}

/* front */
.backup-banner{left:0;top:22px;width:410px;height:58px;background:var(--green);border:2px dashed rgba(255,255,255,.7);border-left:none;color:#fff;font-size:14px;line-height:1.3;padding:8px 10px 0 28px;white-space:nowrap}
.backup-banner b{font-weight:700}
.brand{display:flex;align-items:center;gap:8px;color:var(--blue-dark);font-weight:700;font-size:28px;white-space:nowrap}
.brand-mark{width:22px;height:22px;background:var(--green)}
.front-brand{right:48px;top:30px}
.welcome-band{left:170px;right:0;top:96px;height:56px;background:linear-gradient(90deg,var(--blue-dark),var(--blue));color:#fff;font-size:36px;line-height:56px;padding-left:70px;white-space:nowrap}
.welcome-rule{left:0;width:170px;top:138px;height:8px;background:var(--blue)}
.mission{right:34px;top:160px;width:480px;text-align:right;font-size:13px;line-height:1.3}
.plan-title{right:40px;top:210px;color:var(--green);font-size:30px;line-height:1.2}
.plan-list{right:30px;top:250px;width:370px;list-style:none;text-align:right;font-size:12px;line-height:1.2}
.plan-list li{display:flex;justify-content:flex-end;align-items:flex-start;gap:8px;margin-bottom:4px}
.plan-list svg{flex:none;margin-top:1px}
.photo{border-radius:50%;background:radial-gradient(circle at 45% 40%,#e9e4df,#b8c2c8 70%,#8f9ba2)}
.photo-small{left:40px;top:130px;width:150px;height:150px;border:6px solid var(--green)}
.photo-large{left:40px;top:250px;width:270px;height:270px;border:8px solid var(--blue);background:radial-gradient(circle at 50% 40%,#f1ece8,#c9cfd3 60%,#98a3a9)}
.front-rule{left:0;right:0;top:452px;height:5px;background:var(--blue)}
.front-footer{left:0;right:0;top:460px;bottom:0;background:linear-gradient(180deg,var(--green),var(--green-dark));color:#fff;font-size:20px;font-weight:600;display:flex;justify-content:flex-end;align-items:center;gap:40px;padding-right:40px}
.contact{display:flex;align-items:center;gap:8px}

/* back */
.service-title{color:var(--green);font-size:28px;line-height:1.25;margin-bottom:8px}
.ticks{list-style:none;font-size:13px;line-height:1.3}
.ticks li{display:flex;gap:10px;align-items:flex-start;margin-bottom:8px}
.ticks svg{flex:none;margin-top:2px}
.residential{left:34px;top:24px;width:330px}
.business{left:390px;top:10px;width:320px}
.business .ticks{position:relative}
.business .ticks li.training{position:absolute;left:200px;top:50px}
.col-divider{left:372px;top:20px;width:1px;height:200px;background:#d5d9dc}
.back-brand{left:70px;top:176px;font-size:24px}
.figure{left:250px;top:160px;width:100px;height:66px;border-radius:8px;background:linear-gradient(135deg,#f2f2f2,#c9c9c9 60%,#b23a3a)}
.price-row{left:0;right:0;top:232px;height:80px;display:flex;color:#fff;text-align:center}
.price{display:flex;flex-direction:column;justify-content:center;font-size:24px;line-height:1.1}
.price-single{width:300px;background:var(--blue);padding-top:18px}
.price-family{width:200px;background:var(--dark-band);padding-bottom:10px}
.price-business{flex:1;background:linear-gradient(90deg,var(--blue-dark),var(--blue));padding-bottom:20px}
.about-title{left:40px;top:318px;color:var(--green);font-size:28px;line-height:1.2}
.about-text{left:40px;top:354px;width:340px;font-size:12px;line-height:1.35;text-align:justify}
.about-aside{left:400px;top:322px;width:290px;font-size:12px;line-height:1.35;text-align:justify}
.back-footer{left:0;right:0;top:470px;bottom:0;background:linear-gradient(180deg,var(--green),var(--green-dark));color:#fff;border-top:5px solid var(--blue)}
.address{left:40px;top:6px;font-size:13px;line-height:1.3;display:flex;gap:8px}
.address strong{font-weight:700}
.address small{font-size:10px}
.back-contacts{left:370px;top:10px;font-size:13px;line-height:1.6}
.map{right:30px;top:400px;width:130px;height:130px;border-radius:50%;border:6px solid var(--blue);background:radial-gradient(circle at 40% 45%,#f4f1ea,#dfe5d8 60%,#c5d3bd)}
</style>
</head>
<body>

<section class="card card-front" aria-label="Postcard front">
  <div class="abs backup-banner">We also offer backup services much like vaultmoss<br>but our own brand starting at <b>9.99/month</b></div>
  <div class="abs brand front-brand"><span class="brand-mark"></span>PK Bytes</div>
  <div class="abs welcome-rule"></div>
  <h1 class="abs welcome-band heading">Welcome to PK Bytes Kauai!</h1>
  <div class="abs photo photo-small" role="img" aria-label="Photo of a smiling technician working beside a computer tower"></div>
  <p class="abs mission">Our mission is to alleviate the island's computer problems, educate our ohana to fearlessly embrace technology and practice the art of human interaction.</p>
  <h2 class="abs plan-title heading">Service Plan</h2>
  <ul class="abs plan-list">
    <li><span>Unlimited Virus Removals Only &nbsp;applies to Pcs &amp; Macs<br>($139.99 value)</span><svg width="14" height="12" viewBox="0 0 14 12"><rect x="1" y="1" width="12" height="8" fill="var(--green)" stroke="#333"/><rect x="5" y="9" width="4" height="2" fill="#333"/></svg></li>
    <li><span>Unlimited Computer Tune-ups ($84.99 Value)</span><svg width="14" height="12" viewBox="0 0 14 12"><rect x="1" y="1" width="12" height="8" fill="var(--green)" stroke="#333"/><rect x="5" y="9" width="4" height="2" fill="#333"/></svg></li>
    <li><span>Kauai Based Company</span><svg width="14" height="12" viewBox="0 0 14 12"><rect x="1" y="1" width="12" height="8" fill="var(--green)" stroke="#333"/><rect x="5" y="9" width="4" height="2" fill="#333"/></svg></li>
    <li><span>UnlimitedDevice Setups Get your camera, MP3 player or<br>printer setup</span><svg width="14" height="12" viewBox="0 0 14 12"><rect x="1" y="1" width="12" height="8" fill="var(--green)" stroke="#333"/><rect x="5" y="9" width="4" height="2" fill="#333"/></svg></li>
    <li><span>Includes Internet Security Software ($299.99 value)</span><svg width="14" height="12" viewBox="0 0 14 12"><rect x="1" y="1" width="12" height="8" fill="var(--green)" stroke="#333"/><rect x="5" y="9" width="4" height="2" fill="#333"/></svg></li>
    <li><span>Unlimited Troubleshooting On printers. email and software</span><svg width="14" height="12" viewBox="0 0 14 12"><rect x="1" y="1" width="12" height="8" fill="var(--green)" stroke="#333"/><rect x="5" y="9" width="4" height="2" fill="#333"/></svg></li>
    <li><span>Filtered DNS Service ($49.99/month value)</span><svg width="14" height="12" viewBox="0 0 14 12"><rect x="1" y="1" width="12" height="8" fill="var(--green)" stroke="#333"/><rect x="5" y="9" width="4" height="2" fill="#333"/></svg></li>
    <li><span>Unlimited Remote Supports($84.99 value)</span><svg width="14" height="12" viewBox="0 0 14 12"><rect x="1" y="1" width="12" height="8" fill="var(--green)" stroke="#333"/><rect x="5" y="9" width="4" height="2" fill="#333"/></svg></li>
    <li><span>Free online/Local Backup Software($99.99 Value)</span><svg width="14" height="12" viewBox="0 0 14 12"><rect x="1" y="1" width="12" height="8" fill="var(--green)" stroke="#333"/><rect x="5" y="9" width="4" height="2" fill="#333"/></svg></li>
  </ul>
  <div class="abs front-rule"></div>
  <footer class="abs front-footer">
    <span class="contact"><svg width="18" height="18" viewBox="0 0 24 24"><path d="M6.6 10.8a15 15 0 0 0 6.6 6.6l2.2-2.2c.3-.3.7-.4 1-.2 1.1.4 2.3.6 3.6.6.6 0 1 .4 1 1V20c0 .6-.4 1-1 1A17 17 0 0 1 3 4c0-.6.4-1 1-1h3.5c.6 0 1 .4 1 1 0 1.3.2 2.5.6 3.6.1.3 0 .7-.2 1z" fill="#1f2a30"/></svg>808-317-4962</span>
    <span class="contact"><svg width="18" height="18" viewBox="0 0 24 24"><circle cx="12" cy="12" r="10" fill="none" stroke="#1f2a30" stroke-width="2"/><path d="M2 12h20M12 2c3 3 3 17 0 20M12 2c-3 3-3 17 0 20" fill="none" stroke="#1f2a30" stroke-width="2"/></svg>www.pkbytes.com</span>
  </footer>
  <div class="abs photo photo-large" role="img" aria-label="Photo of a smiling technician leaning on an open computer case"></div>
</section>

<section class="card card-back" aria-label="Postcard back">
  <div class="abs residential">
    <h2 class="service-title heading">Residential Service</h2>
    <ul class="ticks">
      <li><svg width="14" height="14" viewBox="0 0 14 14"><path d="M2 7l3 3 7-8" fill="none" stroke="var(--blue)" stroke-width="2.5"/></svg>SOFTWARE SERVICES</li>
      <li><svg width="14" height="14" viewBox="0 0 14 14"><path d="M2 7l3 3 7-8" fill="none" stroke="var(--blue)" stroke-width="2.5"/></svg>HARDWARE SERVICES</li>
      <li><svg width="14" height="14" viewBox="0 0 14 14"><path d="M2 7l3 3 7-8" fill="none" stroke="var(--blue)" stroke-width="2.5"/></svg>Technical Support (Phone or Remote Desktop)</li>
    </ul>
  </div>
  <div class="abs col-divider"></div>
  <div class="abs business">
    <h2 class="service-title heading">Business Service</h2>
    <ul class="ticks">
      <li><svg width="14" height="14" viewBox="0 0 14 14"><path d="M2 7l3 3 7-8" fill="none" stroke="var(--blue)" stroke-width="2.5"/></svg>SOFTWARE SERVICES</li>
      <li><svg width="14" height="14" viewBox="0 0 14 14"><path d="M2 7l3 3 7-8" fill="none" stroke="var(--blue)" stroke-width="2.5"/></svg>HARDWARE SERVICES</li>
      <li><svg width="14" height="14" viewBox="0 0 14 14"><path d="M2 7l3 3 7-8" fill="none" stroke="var(--blue)" stroke-width="2.5"/></svg>Networking</li>
      <li class="training"><svg width="14" height="14" viewBox="0 0 14 14"><path d="M2 7l3 3 7-8" fill="none" stroke="var(--blue)" stroke-width="2.5"/></svg>Training</li>
      <li><svg width="14" height="14" viewBox="0 0 14 14"><path d="M2 7l3 3 7-8" fill="none" stroke="var(--blue)" stroke-width="2.5"/></svg>MAINTENANCE, CUSTOMIZATION AND<br>TROUBLESHOOTING</li>
      <li><svg width="14" height="14" viewBox="0 0 14 14"><path d="M2 7l3 3 7-8" fill="none" stroke="var(--blue)" stroke-width="2.5"/></svg>Technical Support (Phone or Remote Desktop)</li>
    </ul>
  </div>
  <div class="abs brand back-brand"><span class="brand-mark"></span>PK Bytes</div>
  <div class="abs figure" role="img" aria-label="Illustration of a small white figure pulling a red network cable"></div>

  <div class="abs price-row">
    <div class="price price-single heading">Signle computer<span>24.99/month</span></div>
    <div class="price price-family heading">Family Plan<span>29.99/month</span></div>
    <div class="price price-business heading">Business Plan<span>49.99/per month</span></div>
  </div>

  <h2 class="abs about-title heading">About Us</h2>
  <p class="abs about-text">My name is Kale and I've been working with computers since 1995. My first computer had dial-up internet. Over the years I've tweaked numerous name brand computers, built water-cooled computers and several gaming computers. I founded PK Bytes Inc. on the beautiful island of Kauai, Hawaii, in 2006.</p>
  <p class="abs about-aside">I strive to always provide exceptional customer service in our shop and with our remote support service plans. We also offer hard drives, memory, video cards, etc. on-hand locally.</p>

  <footer class="abs back-footer">
    <div class="abs address">
      <svg width="12" height="16" viewBox="0 0 12 16" style="margin-top:22px"><path d="M6 0a6 6 0 0 0-6 6c0 4.5 6 10 6 10s6-5.5 6-10a6 6 0 0 0-6-6z" fill="#1f2a30"/><circle cx="6" cy="6" r="2.2" fill="#fff"/></svg>
      <div><strong>PkBytes LLC.</strong><br>1845 Niumalu Rd. Suite 210<br>Lihue, Hawaii 96766<br><small>Store hours mon - friday 9am - 6pm</small></div>
    </div>
    <div class="abs back-contacts">
      <div class="contact"><svg width="12" height="12" viewBox="0 0 24 24"><path d="M6.6 10.8a15 15 0 0 0 6.6 6.6l2.2-2.2c.3-.3.7-.4 1-.2 1.1.4 2.3.6 3.6.6.6 0 1 .4 1 1V20c0 .6-.4 1-1 1A17 17 0 0 1 3 4c0-.6.4-1 1-1h3.5c.6 0 1 .4 1 1 0 1.3.2 2.5.6 3.6.1.3 0 .7-.2 1z" fill="#1f2a30"/></svg>808-317-4962</div>
      <div class="contact"><svg width="12" height="12" viewBox="0 0 24 24"><circle cx="12" cy="12" r="10" fill="none" stroke="#1f2a30" stroke-width="2"/><path d="M2 12h20M12 2c3 3 3 17 0 20M12 2c-3 3-3 17 0 20" fill="none" stroke="#1f2a30" stroke-width="2"/></svg>www.pkbytes.com</div>
    </div>
  </footer>
  <div class="abs map" role="img" aria-label="Street map showing the store location in Lihue"></div>
</section>

</body>
</html>
```